Double-sided Business card design needed

I work as an independent consultant in a range of fields, and I need a business card to describes the two main business operations in a two-sided format:

(1) KILT - Kinship Inclusion Learning Therapy

(2) PORT - Promoting Original Regional Tribes

My personal profile so far has been describing myself as:
Dr Gavin Thorpe- Independent R&D Consultant in Community Wellbeing, Education, Mental Health and Disability Support Reform

Industry/Entity Type

Business

Contact Information for Business Card

I need a double-sided business card, describing two different but related businesses that I operate: one in Disability & Mental Health, Education and Community Wellbeing consulting, teaching and research; the other in Indigenous/First Nations-specific community cultural development

Logo Text

See the two business names below for logo text - and they need two different logo designs

Logo styles of interest
Pictorial/Combination Logo

```html
<!DOCTYPE html>
<html lang="en">
<head>
<meta charset="utf-8">
<title>KILT &amp; PORT – Double-sided Business Card</title>
<link rel="stylesheet" href="https://fonts.googleapis.com/css2?family=Open+Sans:wght@400;600;700&display=swap">
<style>
  :root {
    --backdrop: #e7e4e2;
    --card-white: #f7f7f7;
    --teal: #17939e;
    --ink: #1f1f1f;
    --ink-soft: #3a3a3a;
    --band-dark: #202020;
    --white: #ffffff;
  }
  * { box-sizing: border-box; margin: 0; padding: 0; }
  html, body {
    width: 1200px;
    height: 588px;
    overflow: hidden;
    background: var(--backdrop);
    font-family: "Open Sans", sans-serif;
  }
  .canvas { position: relative; width: 1200px; height: 588px; }
  .card {
    position: absolute;
    width: 393px;
    height: 225px;
    border-radius: 10px;
    overflow: hidden;
  }
  .card--kilt { left: 157px; top: 186px; background: var(--card-white); }
  .card--port { left: 660px; top: 188px; background: var(--teal); }

  .brand {
    position: absolute;
    right: 24px;
    top: 22px;
    text-align: right;
  }
  .brand__row {
    display: flex;
    align-items: center;
    justify-content: flex-end;
    gap: 8px;
  }
  .brand__mark {
    width: 14px;
    height: 14px;
  }
  .brand__name {
    font-size: 32px;
    font-weight: 600;
    line-height: 1;
  }
  .brand__tagline {
    font-size: 7px;
    font-weight: 600;
    margin-top: 6px;
    text-transform: uppercase;
  }
  .card--kilt .brand__name { color: var(--teal); }
  .card--kilt .brand__mark { background: var(--teal); }
  .card--kilt .brand__tagline { color: var(--ink); }
  .card--port .brand__name { color: var(--ink); }
  .card--port .brand__mark { background: var(--ink); }
  .card--port .brand__tagline { color: var(--ink); }

  .profile {
    position: absolute;
    left: 22px;
    top: 126px;
  }
  .profile__name {
    font-size: 17px;
    font-weight: 700;
    line-height: 1.2;
  }
  .profile__role {
    font-size: 7.6px;
    line-height: 1.4;
  }
  .card--kilt .profile__name { color: var(--teal); }
  .card--kilt .profile__role { color: var(--ink-soft); }
  .card--port .profile__name { color: var(--white); }
  .card--port .profile__role { color: var(--ink); }

  .contact {
    position: absolute;
    left: 0;
    right: 0;
    top: 180px;
    text-align: center;
    font-size: 9.2px;
    font-weight: 600;
    letter-spacing: 0.6px;
    line-height: 1.55;
    text-transform: uppercase;
    color: var(--ink);
  }
  .band {
    position: absolute;
    left: 0;
    right: 0;
    bottom: 0;
    height: 12px;
  }
  .card--kilt .band { background: var(--teal); }
  .card--port .band { background: var(--band-dark); }
</style>
</head>
<body>
<main class="canvas">
  <section class="card card--kilt" aria-label="Card front: KILT">
    <div class="brand">
      <div class="brand__row">
        <span class="brand__mark"></span>
        <span class="brand__name">KILT</span>
      </div>
      <div class="brand__tagline">Kinship Inclusion Learning Therapy</div>
    </div>
    <div class="profile">
      <h1 class="profile__name">Dr. Gavin Thorpe</h1>
      <p class="profile__role">Independent R&amp;D Consultant in Community Wellbeing,<br>Education, Mental Health and Disability Support Reform</p>
    </div>
    <div class="contact">
      <p>T. 0198 742 365 | E. gavin@kiltcare.com | W. www.kiltcare.com</p>
      <p>Harbour Lane No.18 Westfield City, WF 54321</p>
    </div>
    <div class="band"></div>
  </section>

  <section class="card card--port" aria-label="Card back: PORT">
    <div class="brand">
      <div class="brand__row">
        <span class="brand__mark"></span>
        <span class="brand__name">PORT</span>
      </div>
      <div class="brand__tagline">Promoting Original Regional Tribes</div>
    </div>
    <div class="profile">
      <h2 class="profile__name">Dr. Gavin Thorpe</h2>
      <p class="profile__role">Independent R&amp;D Consultant in Community Wellbeing,<br>Education, Mental Health and Disability Support Reform</p>
    </div>
    <div class="contact">
      <p>T. 0198 742 365 | E. gavin@kiltcare.com | W. www.kiltcare.com</p>
      <p>Harbour Lane No.18 Westfield City, WF 54321</p>
    </div>
    <div class="band"></div>
  </section>
</main>
</body>
</html>
```